Design a 4-page brochure for Bramble Peak Fund

Please use the content from the Updated Brochure attachment to design a 4-page 4-color glossy letter sized brochure for Bramble Peak Fund. The content and concept of the brochure are in the attached word document. Additional photos are attached, and a logo for the fund will be forthcoming (the logo is currently a contest on ArtworkHive)
We own the attached photos that can be used in brochure.

Target Market(s)

Investors

Industry/Entity Type

Investment

```html
<!DOCTYPE html>
<html lang="en">
<head>
<meta charset="utf-8">
<title>Bramble Peak Fund Brochure</title>
<link rel="stylesheet" href="https://fonts.googleapis.com/css2?family=Oswald:wght@600&family=Pathway+Gothic+One&family=Open+Sans:wght@400&display=swap">
<style>
  :root {
    --teal: #3f7f7a;
    --teal-dark: #33706b;
    --paper: #ffffff;
    --panel-grey: #e4e4e4;
    --stage: #e9e9e9;
    --frame: #1e1e1e;
    --text-light: #eef5f4;
  }
  * { box-sizing: border-box; margin: 0; padding: 0; }
  html, body { width: 1200px; height: 900px; overflow: hidden; }
  body {
    background: var(--stage);
    display: flex;
    align-items: center;
    justify-content: center;
    gap: 24px;
  }
  .page {
    width: 556px;
    height: 720px;
    position: relative;
    overflow: hidden;
    box-shadow: 0 6px 18px rgba(0,0,0,0.15);
  }

  /* Cover */
  .cover { background: var(--paper); }
  .brand {
    position: absolute;
    left: 70px;
    top: 120px;
    display: flex;
    align-items: center;
    gap: 14px;
  }
  .brand-square {
    width: 34px; height: 34px;
    border: 3px solid var(--teal);
  }
  .brand-name {
    font-family: "Oswald", sans-serif;
    font-weight: 600;
    font-size: 34px;
    letter-spacing: 1px;
    color: var(--teal);
  }
  .cover-band {
    position: absolute;
    left: 0; right: 0;
    background: var(--teal);
  }
  .cover-band.top { top: 215px; height: 40px; }
  .cover-photo {
    position: absolute;
    left: 0; right: 0;
    top: 255px; height: 205px;
    background: linear-gradient(180deg, #4b4f9c 0%, #6a5fae 45%, #c98a4a 75%, #3b3f6e 100%);
  }
  .cover-band.headline {
    top: 460px; height: 160px;
    padding: 26px 40px 0 40px;
  }
  .headline-text {
    font-family: "Pathway Gothic One", sans-serif;
    font-size: 31px;
    line-height: 1.12;
    text-transform: uppercase;
    color: var(--paper);
  }

  /* Inside bios page */
  .bios { background: var(--panel-grey); }
  .portrait {
    position: absolute;
    left: 70px; right: 40px;
    border-top: 2px solid var(--frame);
    border-bottom: 2px solid var(--frame);
    padding: 8px 0;
  }
  .portrait.upper { top: 30px; }
  .portrait.lower { top: 520px; }
  .portrait-fill { height: 166px; }
  .portrait.upper .portrait-fill {
    background: linear-gradient(135deg, #2c2a26 0%, #4a4d5a 55%, #2f3a55 100%);
  }
  .portrait.lower .portrait-fill {
    background: linear-gradient(135deg, #4c5a34 0%, #7b6a44 50%, #3f4a2c 100%);
  }
  .bio-panel {
    position: absolute;
    left: 0; right: 0;
    top: 230px; height: 270px;
    background: var(--teal-dark);
    padding: 26px 40px;
  }
  .bio-panel p {
    font-family: "Open Sans", sans-serif;
    font-size: 12px;
    line-height: 1.55;
    color: var(--text-light);
    margin-bottom: 12px;
    text-align: justify;
  }
</style>
</head>
<body>
  <section class="page cover">
    <div class="brand">
      <span class="brand-square"></span>
      <span class="brand-name">BRAMBLE PEAK FUND</span>
    </div>
    <div class="cover-band top"></div>
    <div class="cover-photo" role="img" aria-label="Photo of a city skyline at dusk across the water"></div>
    <div class="cover-band headline">
      <h1 class="headline-text">Now you can finally earn substantial monthly returns while realizing solid capital growth</h1>
    </div>
  </section>

  <section class="page bios">
    <div class="portrait upper">
      <div class="portrait-fill" role="img" aria-label="Portrait photo of a fund principal in a suit"></div>
    </div>
    <div class="bio-panel">
      <p>Mr. Halvorsen brings over twenty years of entrepreneurial experience to the fund. He has a background in implementing strategic plans to increase revenue, with an emphasis on sales management and business development. He has been a co-founder in a number of early stage companies, raising over thirty million dollars in growth financing.</p>
      <p>Mr. Halvorsen chaired the Sales Advisory Council and helped write the procedures into policy. He was named Sales Representative of the Year at Meridell Health and later led financial research at Ashcombe and Company. He started his career at Corvane Systems and won a national championship in rowing at university.</p>
    </div>
    <div class="portrait lower">
      <div class="portrait-fill" role="img" aria-label="Outdoor portrait photo of a second fund principal"></div>
    </div>
  </section>
</body>
</html>
```